Letter Head Design

I need a letter head design based on my company logo that I attached.
Include phone number: (403)582-3140
Address: 417 Brindlewood Avenue NE, Calgary, Alberta, Canada, T3M 4K8

Industry/Entity Type

It Company

```html
<!DOCTYPE html>
<html lang="en">
<head>
<meta charset="utf-8">
<title>Lumenhall Interiors Corp. Letterhead</title>
<link rel="stylesheet" href="https://fonts.googleapis.com/css2?family=Arimo:wght@400;700&family=Tinos&display=swap">
<style>
  :root {
    --backdrop: #e9e7e4;
    --paper: #ffffff;
    --brand-blue: #2a5bd6;
    --brand-green: #5ccb2a;
    --band-deep: #1536d4;
    --band-light: #3fa6f2;
    --faint-mark: #f6f9fd;
    --faint-edge: #eef3fa;
    --footer-text: #ffffff;
  }
  html, body {
    margin: 0;
    padding: 0;
    width: 956px;
    height: 1200px;
    overflow: hidden;
    background: var(--backdrop);
  }
  .letterhead {
    position: absolute;
    left: 53px;
    top: 62px;
    width: 848px;
    height: 1098px;
    background: var(--paper);
    overflow: hidden;
  }
  .brand {
    position: absolute;
    left: 20px;
    top: 26px;
  }
  .brand-square {
    width: 72px;
    height: 72px;
    margin-left: 35px;
    border-radius: 6px;
    background: var(--brand-green);
  }
  .brand-name {
    margin: 9px 0 0;
    font-family: "Arimo", sans-serif;
    font-weight: 400;
    font-size: 21px;
    line-height: 1;
    color: var(--brand-blue);
    white-space: nowrap;
  }
  .faint-mark {
    position: absolute;
    left: 187px;
    top: 343px;
    width: 467px;
    height: 467px;
    box-sizing: border-box;
    border-radius: 34px;
    border: 18px solid var(--faint-edge);
    background: var(--faint-mark);
  }
  .footer-band {
    position: absolute;
    left: 0;
    bottom: 0;
    width: 848px;
    height: 110px;
  }
  .footer-contact {
    position: absolute;
    left: 20px;
    bottom: 13px;
    margin: 0;
    font-family: "Tinos", serif;
    font-size: 15.5px;
    line-height: 23px;
    color: var(--footer-text);
  }
  .footer-contact .phone-icon {
    width: 13px;
    height: 13px;
    vertical-align: -1px;
    margin-right: 5px;
  }
</style>
</head>
<body>
  <main class="letterhead">
    <header class="brand">
      <div class="brand-square"></div>
      <p class="brand-name">Lumenhall Interiors Corp.</p>
    </header>

    <div class="faint-mark"></div>

    <footer>
      <svg class="footer-band" viewBox="0 0 848 110" preserveAspectRatio="none" aria-hidden="true">
        <defs>
          <radialGradient id="bandGlow" cx="0.45" cy="0.75" r="0.6">
            <stop offset="0" stop-color="var(--band-light)"/>
            <stop offset="1" stop-color="var(--band-deep)"/>
          </radialGradient>
        </defs>
        <path d="M0,22 Q430,-18 848,60 L848,70 Q430,-4 0,28 Z" fill="var(--brand-green)"/>
        <path d="M0,34 Q430,4 848,76 L848,110 L0,110 Z" fill="url(#bandGlow)"/>
      </svg>
      <p class="footer-contact">
        <svg class="phone-icon" viewBox="0 0 24 24" aria-hidden="true"><path fill="#ffffff" d="M6.6 10.8a15.1 15.1 0 0 0 6.6 6.6l2.2-2.2a1 1 0 0 1 1-.25 11.4 11.4 0 0 0 3.6.57 1 1 0 0 1 1 1V20a1 1 0 0 1-1 1A17 17 0 0 1 3 4a1 1 0 0 1 1-1h3.5a1 1 0 0 1 1 1c0 1.25.2 2.45.57 3.6a1 1 0 0 1-.25 1z"/></svg>(403)582-3140<br>
        417 Brindlewood Avenue NE, Calgary&nbsp; Alberta, Canada, T3M 4K8
      </p>
    </footer>
  </main>
</body>
</html>
```